Info flyer to showcase security camera install and remote video monitoring.

I am looking for an attractive looking flyer that is simple and has some text content and some photos to show prospective clients what services I can provide them.

The two main services that I want to showcase are:
1. Security Camera & NVR Installations and maintenance
2. Remote Video Monitoring for business. This can be a temporary service or ongoing/long term.

Target Market(s)

Construction, Retail, Industrial, Commercial

Industry/Entity Type

Security

Font styles to use
Serif

Colors

Designer to choose colors to be used in the design.

```html
<!DOCTYPE html>
<html lang="en">
<head>
<meta charset="utf-8">
<title>Vantage Integrated Solutions – Security Flyer</title>
<link rel="stylesheet" href="https://fonts.googleapis.com/css2?family=Bebas+Neue&display=swap">
<style>
  :root {
    --backdrop: #4a4446;
    --paper: #ffffff;
    --ink: #222226;
    --gold: #d9a02e;
    --gold-deep: #c4902a;
    --gold-light: #ecc987;
    --sky: #2f7cc4;
  }
  * { margin: 0; padding: 0; box-sizing: border-box; }
  html, body { width: 1200px; height: 1200px; overflow: hidden; background: var(--backdrop); }
  .flyer {
    position: absolute; left: 50px; top: 250px;
    width: 1100px; height: 700px;
    background: var(--paper); overflow: hidden;
    font-family: "Bebas Neue", "Arial Narrow", sans-serif;
    color: var(--ink);
  }
  .flyer-shapes { position: absolute; inset: 0; }
  .brand {
    position: absolute; left: 420px; top: 38px;
    display: flex; align-items: center; gap: 16px;
    white-space: nowrap;
  }
  .brand-dot { width: 66px; height: 66px; border-radius: 50%; background: var(--ink); flex: none; }
  .brand-name { line-height: 0.9; color: var(--ink); }
  .brand-name .main { display: block; font-size: 96px; letter-spacing: 4px; }
  .brand-name .sub { display: block; font-size: 34px; letter-spacing: 3px; }
  .photo {
    position: absolute; border: 2px solid var(--gold);
    background: linear-gradient(160deg, #4a93d6, var(--sky));
  }
  .photo-dome { left: 120px; top: 188px; width: 235px; height: 140px; }
  .photo-bullet { left: 370px; top: 188px; width: 245px; height: 140px; }
  .photo-circle {
    position: absolute; left: 700px; top: 192px; width: 340px; height: 340px;
    border-radius: 50%;
    background: radial-gradient(circle at 45% 40%, #f1f1ee 0 30%, #9db3c4 55%, #3e6f93 100%);
  }
  .service { position: absolute; white-space: nowrap; }
  .service h2 { font-weight: 400; color: var(--gold); font-size: 46px; line-height: 1; letter-spacing: 1px; }
  .service p { font-size: 28px; line-height: 1; letter-spacing: 0.5px; }
  .service-install { left: 200px; top: 344px; }
  .service-monitor { left: 60px; top: 444px; }
  .divider { position: absolute; left: 200px; top: 430px; width: 440px; height: 1px; background: var(--gold); }
  .contact-bar {
    position: absolute; left: 0; top: 560px; width: 1100px; height: 100px;
    display: flex; align-items: center; justify-content: space-around;
    color: var(--gold); font-size: 30px; letter-spacing: 0.5px;
  }
  .contact-item { display: flex; flex-direction: column; align-items: center; gap: 6px; }
  .contact-sep { width: 1px; height: 50px; background: var(--gold); }
  .contact-item svg { width: 30px; height: 30px; }
</style>
</head>
<body>
<main class="flyer">
  <svg class="flyer-shapes" viewBox="0 0 1100 700" aria-hidden="true">
    <path fill="var(--gold-light)" d="M950,0 H1100 V560 H520 C760,540 900,460 960,330 C1010,220 1000,100 950,0Z"/>
    <path fill="var(--ink)" d="M1000,0 H1100 V560 H560 C800,540 930,470 990,340 C1040,230 1045,110 1000,0Z"/>
    <path fill="var(--gold-deep)" d="M1100,230 V560 H420 C700,545 900,500 1000,400 C1060,340 1090,290 1100,230Z"/>
    <rect x="0" y="560" width="1100" height="100" fill="var(--ink)"/>
    <rect x="0" y="660" width="1100" height="40" fill="var(--gold)"/>
  </svg>

  <div class="brand">
    <span class="brand-dot"></span>
    <span class="brand-name"><span class="main">VANTAGE</span><span class="sub">INTEGRATED SOLUTIONS</span></span>
  </div>

  <div class="photo photo-dome" role="img" aria-label="Photo of a white dome security camera on a pole against blue sky"></div>
  <div class="photo photo-bullet" role="img" aria-label="Photo of several bullet security cameras mounted on a pole against blue sky"></div>
  <div class="photo-circle" role="img" aria-label="Photo of a ceiling-mounted dome security camera in a retail interior"></div>

  <section class="service service-install">
    <h2>Security Camera &amp; NVR</h2>
    <p>Installations and Maintenance</p>
  </section>
  <div class="divider"></div>
  <section class="service service-monitor">
    <h2>Remote Video Monitoring for Business</h2>
    <p>This can be a temporary service or ongoing/long term.</p>
  </section>

  <footer class="contact-bar">
    <div class="contact-item">
      <svg viewBox="0 0 30 30" fill="none" stroke="var(--gold)" stroke-width="2"><circle cx="15" cy="15" r="13"/><ellipse cx="15" cy="15" rx="6" ry="13"/><line x1="2" y1="15" x2="28" y2="15"/><line x1="4" y1="8" x2="26" y2="8"/><line x1="4" y1="22" x2="26" y2="22"/></svg>
      <span>www.vantagesecure.com</span>
    </div>
    <span class="contact-sep"></span>
    <div class="contact-item">
      <svg viewBox="0 0 30 30"><rect x="2" y="7" width="26" height="17" fill="var(--gold)"/><path d="M2,7 L15,17 L28,7" fill="none" stroke="var(--ink)" stroke-width="2"/></svg>
      <span>vantage@secure.com</span>
    </div>
    <span class="contact-sep"></span>
    <div class="contact-item">
      <svg viewBox="0 0 30 30" fill="none" stroke="var(--gold)" stroke-width="2"><rect x="9" y="2" width="12" height="26" rx="2"/><line x1="13" y1="24" x2="17" y2="24"/></svg>
      <span>0002 - 5555 - 3100</span>
    </div>
  </footer>
</main>
</body>
</html>
```